Business card design needed

We are a Landscape business based in Sydney. We are targeting upper class clients that have the money to spend on their gardens.
We design, construct and maintain the gardens that we create.
We are looking for modern business card with our logo on it and the colours green grey\black/white scale. The design should communicate modern creative gardens. it should look classy and have a professional feel to it not cheap.should be two sides to the business card. Back side to have the words design construct maintain with possible the vine attached somewhere.
Updates

Project Deadline Extended
Reason: Hi Guys. Some of you have asked for a vector version of the vine so I just need some more time to find it as I don't have it here on my computer. Keep up the good work! Thanks Jon

Hi guys and girls.
You have all done a really good job so far. I have recently uploaded the vector for the vine and the logo as promissed. Looking forward to seeing you use them in your designs. Also i would like to see the words design-construct-maintain on the card as an option maybe on the back.
Thanks .

Target Market(s)

white collar, higher education, high social group in affluent areas

Industry/Entity Type

Business

Contact Information for Business Card

Bright Meadow Landscapes
Jonathan Perrow- 0431 592 740 Director( only need one name and number per card i.e. same design twice with different number and name.)
Paul tremaine- 0417 365 209 Director
www.bmlandscapes.example.au
ABN-872 310 954
Lic- 618094K

Requirements
Must have
• Logo which I am trying to upload but it is not working. I have contacted sketch forge to try and fix this.
Should not have
• Two s

```html
<!DOCTYPE html>
<html lang="en">
<head>
<meta charset="utf-8">
<title>Bright Meadow Landscapes – Business Card</title>
<link rel="stylesheet" href="https://fonts.googleapis.com/css2?family=Open+Sans:wght@400;600;700&display=swap">
<style>
  :root {
    --stage: #1c1c1d;
    --card-top: #4a4d4d;
    --card-bottom: #363939;
    --lime: #8dc63f;
    --lime-soft: rgba(141, 198, 63, 0.55);
    --white: #f4f4f2;
    --muted: #c9cbca;
    --vine-white: rgba(240, 240, 236, 0.55);
  }
  * { box-sizing: border-box; margin: 0; padding: 0; }
  html, body {
    width: 1200px; height: 900px; overflow: hidden;
    background: var(--stage);
    font-family: "Open Sans", Arial, sans-serif;
  }
  .canvas {
    width: 1200px; height: 900px;
    display: flex; align-items: center; justify-content: center; gap: 40px;
  }
  .card {
    position: relative;
    width: 540px; height: 330px;
    border-radius: 18px;
    background: linear-gradient(160deg, var(--card-top), var(--card-bottom));
    overflow: hidden;
    color: var(--white);
  }

  /* Front */
  .brand { position: absolute; left: 34px; top: 118px; }
  .brand-name {
    font-size: 22px; font-weight: 600; letter-spacing: 0.5px;
    color: var(--white); line-height: 1.2; width: 230px;
  }
  .services {
    position: absolute; left: 40px; top: 190px;
    list-style: none; font-size: 14px; line-height: 1.3; color: var(--white);
  }
  .services li::before {
    content: "•"; color: var(--lime); margin-right: 6px;
  }
  .services li.continued { padding-left: 13px; }
  .front .vine {
    position: absolute; right: 0; top: 0; width: 300px; height: 250px;
    background: radial-gradient(ellipse at 70% 40%, var(--vine-white), var(--lime-soft) 40%, rgba(141,198,63,0) 75%);
  }
  .front .dots {
    position: absolute; left: 0; bottom: 0; width: 200px; height: 90px;
    background: radial-gradient(ellipse at 20% 100%, rgba(141,198,63,0.35), rgba(141,198,63,0) 70%);
  }

  /* Back */
  .back .brand { left: 150px; top: 58px; }
  .back .vine {
    position: absolute; right: 0; top: 40px; width: 260px; height: 290px;
    background: radial-gradient(ellipse at 60% 50%, rgba(255,255,255,0.09), rgba(255,255,255,0) 70%);
  }
  .registration {
    position: absolute; right: 40px; top: 24px;
    font-size: 9px; line-height: 1.35; color: var(--muted);
  }
  .contact { position: absolute; left: 40px; top: 170px; }
  .contact-name { font-size: 22px; color: var(--lime); font-weight: 400; }
  .contact-role { font-size: 14px; font-weight: 700; margin-top: -2px; }
  .contact-phone { font-size: 16px; margin-top: 14px; letter-spacing: 0.5px; }
  .contact-email { font-size: 16px; margin-top: 16px; }
  .contact-web { font-size: 16px; }
  .contact-web .domain { color: var(--lime); }
</style>
</head>
<body>
<main class="canvas">
  <section class="card front">
    <div class="vine" role="img" aria-label="Flowing green and white vine ornament with leaves"></div>
    <div class="dots" role="img" aria-label="Soft green halftone dot pattern"></div>
    <div class="brand">
      <p class="brand-name">Bright Meadow Landscapes</p>
    </div>
    <ul class="services">
      <li>Horticultural Concept</li>
      <li class="continued" style="list-style:none">&amp; Design</li>
      <li>Stone/Slate/Sandstone</li>
      <li>Water Features</li>
      <li>Timber/Decks</li>
      <li>Paving</li>
      <li>Turf</li>
    </ul>
  </section>

  <section class="card back">
    <div class="vine" role="img" aria-label="Faint tone-on-tone vine ornament"></div>
    <p class="registration">ABN-872 310 954<br>Lic- 618094K</p>
    <div class="brand">
      <p class="brand-name">Bright Meadow Landscapes</p>
    </div>
    <div class="contact">
      <p class="contact-name">Jonathan Perrow</p>
      <p class="contact-role">Director</p>
      <p class="contact-phone">0431 592 740</p>
      <p class="contact-email">bmlandscapes@mailbox.example.au</p>
      <p class="contact-web">www.<span class="domain">bmlandscapes</span>.example.au</p>
    </div>
  </section>
</main>
</body>
</html>
```